Photo/Video Company needs a business card design

We need a business card design for a photo/video production company called 'Corvane Studio'. We primarily do wedding photography and videography, however we also do commercial, corporate, and promo work.

We would like a clean, white design that primarily markets us as a wedding photo/video company, but still sleek enough that we attract corporate and commercial clients.

Industry/Entity Type

Wedding

Requirements
Must have
• We wish the front of the business card to simply have the logo, and the back will have the contact information:

Corvane Studio
Wedding, Event, Corporate, Commercial, Promo
647-518-2063
info@corvanestudio.example
www.corvanestudio.example

We are hoping for a version of the card that has only the companies name on it, as well as several variations that have different employees names printed.

The employee names and titles are:

Tom Belliwe - Photo/Video
Deklan Belliwe - Photo/Video
Pieter Walcox -Video
Lydia Prohane -Photo/Video

The design should use similar fonts in the writing as the fonts used in the logo design. The AI file will be provided.
Nice to have
• We also might like to see the front of the card have the main logo, as well as 'Wedding, Event, Corporate, Commercial, Promo' written in the bottom corner.
Should not have
• No old style fonts should be used. Also no other graphic images should be created, but we are open to the possibility of having shapes and borders.

```html
<!DOCTYPE html>
<html lang="en">
<head>
<meta charset="utf-8">
<title>Corvane Studio – Business Card</title>
<link href="https://fonts.googleapis.com/css2?family=Questrial&display=swap" rel="stylesheet">
<style>
  :root {
    --paper: #ffffff;
    --frame: #8a8a8a;
    --card-edge: #4a4a4a;
    --band-grey: #e9eaec;
    --accent-red: #d9231f;
    --ink: #3a3a3a;
    --ink-soft: #555555;
  }
  * { box-sizing: border-box; margin: 0; padding: 0; }
  html, body {
    width: 1200px;
    height: 900px;
    overflow: hidden;
    background: var(--paper);
    font-family: "Questrial", "Century Gothic", sans-serif;
  }
  .sheet {
    position: relative;
    width: 1200px;
    height: 900px;
  }
  .sheet-frame {
    position: absolute;
    inset: 4px;
    border: 1px solid var(--frame);
  }
  .card {
    position: absolute;
    left: 280px;
    width: 650px;
    height: 382px;
    border: 1.5px solid var(--card-edge);
    background: var(--paper);
    overflow: hidden;
  }
  .card--front { top: 50px; }
  .card--back { top: 476px; }
  .card-sweep {
    position: absolute;
    inset: 0;
    width: 100%;
    height: 100%;
  }
  .sweep-band { fill: var(--band-grey); }
  .sweep-accent { fill: var(--accent-red); }

  .brand-mark {
    position: absolute;
    left: 50px;
    top: 222px;
    width: 34px;
    height: 34px;
    background: var(--accent-red);
  }
  .brand-name {
    position: absolute;
    left: 104px;
    top: 212px;
    font-size: 41px;
    line-height: 1;
    letter-spacing: 0.5px;
    color: var(--ink);
    white-space: nowrap;
  }
  .brand-tagline {
    position: absolute;
    left: 262px;
    top: 263px;
    font-size: 11px;
    letter-spacing: 8px;
    color: var(--ink);
    white-space: nowrap;
  }

  .contact {
    position: absolute;
    left: 22px;
    top: 246px;
    list-style: none;
    font-size: 19px;
    line-height: 24.5px;
    color: var(--ink-soft);
  }
</style>
</head>
<body>
<main class="sheet">
  <div class="sheet-frame"></div>

  <section class="card card--front" aria-label="Card front">
    <svg class="card-sweep" viewBox="0 0 650 382" preserveAspectRatio="none" aria-hidden="true">
      <polygon class="sweep-band" points="50,0 180,0 650,120 650,165"/>
      <polygon class="sweep-accent" points="536,76 650,10 650,48 588,76"/>
    </svg>
    <span class="brand-mark" aria-hidden="true"></span>
    <h1 class="brand-name">CORVANE STUDIO</h1>
    <p class="brand-tagline">photo + cinema</p>
  </section>

  <section class="card card--back" aria-label="Card back">
    <svg class="card-sweep" viewBox="0 0 650 382" preserveAspectRatio="none" aria-hidden="true">
      <polygon class="sweep-band" points="50,0 180,0 650,120 650,165"/>
      <polygon class="sweep-accent" points="536,76 650,10 650,48 588,76"/>
    </svg>
    <ul class="contact">
      <li class="contact-name">Corvane Studio</li>
      <li class="contact-services">Wedding, Event, Corporate, Commercial, Promo</li>
      <li class="contact-phone">647-518-2063</li>
      <li class="contact-email">info@corvanestudio.example</li>
      <li class="contact-web">www.corvanestudio.example</li>
    </ul>
  </section>
</main>
</body>
</html>
```